Business Card for a finance professional

I need a business card design to introduce myself to a professional networking (mainly banks) and potential companies to hire and remember me. I would like to use black, grey, white and maybe gold/silver colors and maybe something with my initials(R L F P T). The final design should communicate seriousness, profissionalism and something innovative.

The basic informations in the card are: Name, e-mail, phone number and trabnet. (I'm thinking to put some directly short link to my trabnet account or maybe some app - non QR Code - to add my contacts to a phone directly.)

My name is Mariana Lopes Ferreira Pinto dos Reis (I prefer to use only 'Mariana Lopes' or 'Mariana Reis' but i'm open to other suggestions) and I have 26 years old (just if it helps to build based in my age).
Updates

Dear designers, I wish to thank your participation in this project! It was very difficult to choose one! Thank your for your work! Best regards and success. Mariana

Target Market(s)

Potential hires and big companies.

Industry/Entity Type

Finance

Requirements
Must have
• The informations required at the business card are:
Name: Mariana Lopes F. P. dos Reis
Email: mariana.lop.reis@quellomail.com
Phone: +55 61 8493 5710
TrabNet: http://br.trabnet-perfis.com/in/marianalr/
Nice to have
• Modern and innovative look.
I suggest to use the colors black, grey, white, gold and/or silver, but I'm open to other colors.
Should not have
• A message showing that I need to be hired. It's more to "know me and remember me" than "hire me please".

```html
<!DOCTYPE html>
<html lang="en">
<head>
<meta charset="utf-8">
<title>Mariana Reis – Business Card</title>
<link rel="stylesheet" href="https://fonts.googleapis.com/css2?family=Comfortaa:wght@700&family=Questrial&display=swap">
<style>
  :root {
    --page-bg: #e8e5de;
    --card-white: #ffffff;
    --card-grey: #ececec;
    --ink-brown: #4b3b29;
    --ink-grey: #555555;
    --pattern-light: #e4e4e4;
    --pattern-dark: #cfcfcf;
    --strip-bg: #f2f2f2;
  }
  html, body {
    margin: 0;
    padding: 0;
    width: 1200px;
    height: 1000px;
    overflow: hidden;
    background: var(--page-bg);
  }
  .canvas {
    position: relative;
    width: 1200px;
    height: 1000px;
  }
  .card {
    position: absolute;
    left: 300px;
    width: 600px;
    height: 340px;
    background: linear-gradient(160deg, var(--card-white) 0%, var(--card-grey) 100%);
    box-shadow: 0 6px 18px rgba(0,0,0,0.18);
    overflow: hidden;
  }
  .card--front { top: 90px; }
  .card--back { top: 560px; }

  .initials-pattern {
    position: absolute;
    top: 0;
    bottom: 0;
    background: linear-gradient(170deg, var(--pattern-light) 0%, var(--pattern-dark) 100%);
  }
  .card--front .initials-pattern { right: 0; width: 180px; }
  .card--back .initials-pattern { left: 0; width: 440px; }

  .name-block {
    position: absolute;
    left: 60px;
    top: 120px;
    color: var(--ink-brown);
    font-family: "Comfortaa", sans-serif;
    font-weight: 700;
    line-height: 1;
  }
  .name-block__first {
    display: block;
    font-size: 60px;
    letter-spacing: -1px;
  }
  .name-block__last {
    display: block;
    font-size: 50px;
    margin-top: 2px;
  }

  .contact-strip {
    position: absolute;
    right: 0;
    top: 0;
    width: 160px;
    height: 340px;
    background: var(--strip-bg);
  }
  .contact-list {
    position: absolute;
    inset: 0;
    margin: 0;
    padding: 22px 24px;
    list-style: none;
    writing-mode: vertical-rl;
    transform: rotate(180deg);
    font-family: "Questrial", sans-serif;
    font-size: 12.5px;
    color: var(--ink-grey);
    line-height: 2.1;
    text-align: end;
  }
</style>
</head>
<body>
<main class="canvas">
  <section class="card card--front" aria-label="Business card front">
    <div class="name-block">
      <span class="name-block__first">MARIANA</span>
      <span class="name-block__last">Reis</span>
    </div>
    <div class="initials-pattern" role="img" aria-label="Repeating grey pattern of the initials R L F P T"></div>
  </section>

  <section class="card card--back" aria-label="Business card back">
    <div class="initials-pattern" role="img" aria-label="Repeating grey pattern of the initials R L F P T"></div>
    <div class="contact-strip">
      <ul class="contact-list">
        <li>Mariana Lopes F. P. dos Reis</li>
        <li>Phone: +55 61 8493 5710</li>
        <li>Email: mariana.lop.reis@quellomail.com</li>
        <li>TrabNet: http://br.trabnet-perfis.com/in/marianalr/</li>
      </ul>
    </div>
  </section>
</main>
</body>
</html>
```